Business card design for Velvet Harbor

We need business cards designed for our new marketing consulting company, Velvet Harbor. Our services include marketing strategy, go-to-market and launch planning, growth strategy, and execution. We serve medical technology and health technology companies, from startups to well-established growth companies.

The business cards should feel professional, credible, reliable and trustworthy, and should instill confidence. Also bold, creative, and modern.

The design must use the Velvet Harbor logo.

The primary brand color is this orange: #FF5501
A secondary color that you can use is this gray: #282B2D
I would prefer only to use the orange and gray. But if you feel you really need an additional accent color (please use it very sparingly, as little as possible), you can use this blue for small accent purposes: #009FED

Attached are the logo files. The main logo is the one with a little bit of orange on the left and the rest is gray.

The business card should include the following:

Velvet Harbor logo
First name and last name
Title
Email address
Phone number and type (in whatever order looks best for the design
Website (the website does not need to be in the same block as the personal info)

For example:

Nessa Pryle
Founder & Principal
nessa@velvetharbor.com
+1.628.309.4156 mobile (can use "." or spaces in between blocks of numbers)
velvetharbor.com (somewhere on the card, it does not need to be with the personal info; and note that there is no "www." at the beginning)

Note that there will be no address listed on the business card.

Target Market(s)

Executives (CEO, head of marketing, head of sales) at medical technology and health technology companies, mostly in their 40s and older, well-educated, often with advanced degrees. They are strategic thinkers, responsible for budgets, and familiar with P&L. Their comfort with and trust in using outside consultants varies.

Industry/Entity Type

Medical technology and health technology companies.

Contact Information for Business Card

See project description

Font styles to use
Sans Serif

Requirements
Must have
• Logo and see Business card details section above.

```html
<!DOCTYPE html>
<html lang="en">
<head>
<meta charset="utf-8">
<title>Velvet Harbor — Business Card</title>
<link rel="stylesheet" href="https://fonts.googleapis.com/css2?family=Lato:ital,wght@0,400;0,700;1,900&display=swap">
<style>
  :root {
    --brand-orange: #FF5501;
    --brand-gray: #282B2D;
    --card-white: #FFFFFF;
    --backdrop: #E4E5E7;
    --text-light: #F2F2F2;
  }
  * { box-sizing: border-box; margin: 0; padding: 0; }
  html, body {
    width: 1200px;
    height: 1200px;
    overflow: hidden;
  }
  body {
    background: var(--backdrop);
    font-family: "Lato", Arial, sans-serif;
    position: relative;
  }
  .card {
    position: absolute;
    left: 162px;
    width: 874px;
    height: 512px;
    box-shadow: 0 10px 30px rgba(0, 0, 0, 0.18);
  }
  .card--front {
    top: 77px;
    background: var(--brand-gray);
  }
  .card--back {
    top: 617px;
    background: var(--card-white);
    display: flex;
    align-items: center;
    justify-content: center;
  }

  /* Front: personal details */
  .identity {
    position: absolute;
    right: 176px;
    top: 128px;
    text-align: right;
  }
  .identity__name {
    font-weight: 900;
    font-style: italic;
    font-size: 36px;
    letter-spacing: -0.5px;
    color: var(--brand-orange);
    text-transform: uppercase;
    line-height: 1;
  }
  .identity__title {
    margin-top: 8px;
    font-size: 21px;
    color: var(--text-light);
    line-height: 1.2;
  }
  .contact-list {
    position: absolute;
    right: 140px;
    top: 254px;
    list-style: none;
    text-align: right;
  }
  .contact-list__item {
    display: flex;
    align-items: center;
    justify-content: flex-end;
    gap: 18px;
    font-size: 21px;
    color: var(--text-light);
    height: 34px;
  }
  .contact-list__item--web { margin-top: 24px; }
  .contact-list__icon {
    width: 18px;
    height: 18px;
    flex: none;
  }

  /* Back: wordmark */
  .wordmark {
    display: flex;
    align-items: center;
    gap: 34px;
  }
  .wordmark__dot {
    width: 26px;
    height: 26px;
    border-radius: 50%;
    background: var(--brand-orange);
    flex: none;
  }
  .wordmark__name {
    font-weight: 700;
    font-size: 54px;
    letter-spacing: 14px;
    line-height: 1.02;
    text-transform: uppercase;
    color: var(--brand-gray);
  }
</style>
</head>
<body>

  <section class="card card--front" aria-label="Business card front">
    <div class="identity">
      <h1 class="identity__name">Nessa Pryle</h1>
      <p class="identity__title">Founder &amp; Principal</p>
    </div>

    <ul class="contact-list">
      <li class="contact-list__item">
        <span>+1.628.309.4156</span>
        <svg class="contact-list__icon" viewBox="0 0 18 18" aria-label="mobile">
          <rect x="4.5" y="1" width="9" height="16" rx="1.6" fill="none" stroke="var(--brand-orange)" stroke-width="1.8"/>
          <circle cx="9" cy="14" r="1" fill="var(--brand-orange)"/>
        </svg>
      </li>
      <li class="contact-list__item">
        <span>nessa@velvetharbor.com</span>
        <svg class="contact-list__icon" viewBox="0 0 18 18" aria-label="email">
          <rect x="1.5" y="3.5" width="15" height="11" rx="1.5" fill="var(--brand-orange)"/>
          <path d="M2.5 5 L9 10 L15.5 5" fill="none" stroke="var(--brand-gray)" stroke-width="1.4"/>
        </svg>
      </li>
      <li class="contact-list__item contact-list__item--web">
        <span>velvetharbor.com</span>
        <svg class="contact-list__icon" viewBox="0 0 18 18" aria-label="website">
          <circle cx="9" cy="9" r="7" fill="none" stroke="var(--brand-orange)" stroke-width="1.6"/>
          <ellipse cx="9" cy="9" rx="3" ry="7" fill="none" stroke="var(--brand-orange)" stroke-width="1.2"/>
          <path d="M2 9 H16 M3.2 5.5 H14.8 M3.2 12.5 H14.8" stroke="var(--brand-orange)" stroke-width="1.2"/>
        </svg>
      </li>
    </ul>
  </section>

  <section class="card card--back" aria-label="Business card back">
    <div class="wordmark">
      <span class="wordmark__dot"></span>
      <p class="wordmark__name">Velvet<br>Harbor</p>
    </div>
  </section>

</body>
</html>
```